Harbor Wellness Partners -Postcard Design

New Post Card design for a new company based in Florida called "Harbor Wellness Partners". Our website is www.harborwellnesspartners-example.com, our phone is 855-HARBR22 (855-427-2722). We offer a no fee service to help our clients find suitable alcohol/drug abuse/addition treatment so that they can attain LONG-TERM recovery.
The facilities we work with have been hand chosen by us after a rigorous interview process.
We have facilities that use various approaches to suit the needs of the client wanting Long-Term Recovery. Evidence based, 12-step based, christian based, and alternative healing based.
Feel free to add a "tag line" that you think will catch attention. We use..."We help our clients drop anchor in Long-Term Recovery". "Call 1-855-HARBR22 before you have to call 911". "Long-Term recovery is our goal, not temporary sobriety."
We interview the treatment facilities to ensure that top treatment is given to our clients, we don't put there where they will not get the care promised.
Some services we can place for are: Interventions, Detox, Partial Hospitalization Program (PHP), Intensive Out Patient (IOP), Out Patient (OP), Sober Living Communities.
Several facilities with several approaches to treatment & recovery.

I am not a designer, so leaving entire design options open (eg...colors, graphics, fonts, etc....) Postcard size will be either 6 x 4 or 7 x 5.

Target Market(s)

Target Market for these postcards are treatment facilities & potential clients around the country. To give them someone to call for help in placing alcoholics & addicting into treatment facilities with different approaches.

Industry/Entity Type

It Company

Requirements
Must have
• THESE DO NOT HAVE TO BE EXACT WORDING!!
• The facilities we work with have been hand chosen by us after a rigorous interview process.
• Treatment programs: Detox, In-Patient, Partial Hospitalization Program (PHP), Intensive out patient (IOP), Out Patient, Sober Living Communities.
• We have facilities that use various approaches to suit the needs of the client wanting Long-Term Recovery. Evidence based, 12-step based, christian based, and alternative healing based.

```html
<!DOCTYPE html>
<html lang="en">
<head>
<meta charset="UTF-8">
<title>Harbor Wellness Partners – Postcard</title>
<link rel="stylesheet" href="https://fonts.googleapis.com/css2?family=Inter:wght@300;800&family=Carlito&family=Arimo:wght@400;700&display=swap">
<style>
  :root {
    --brown: #5b2b15;
    --gold: #f4cd6c;
    --white: #ffffff;
    --paper: #ffffff;
    --ink: #1f1f1f;
    --tag-brown: #6a2e14;
  }
  * { margin: 0; padding: 0; box-sizing: border-box; }
  html, body { width: 924px; height: 1200px; overflow: hidden; background: var(--paper); }
  .postcard {
    position: relative;
    width: 924px;
    height: 1200px;
    background: var(--brown);
    overflow: hidden;
  }
  .hero-photo {
    position: absolute;
    inset: 0 0 auto 0;
    height: 640px;
    background:
      radial-gradient(ellipse at 60% 35%, rgba(230,190,110,0.55) 0%, rgba(230,190,110,0) 45%),
      linear-gradient(180deg, #8a8a5a 0%, #6f6848 18%, #6b5a40 38%, #6a4630 58%, var(--brown) 100%);
  }
  .headline {
    position: absolute;
    left: 70px;
    top: 282px;
    color: var(--gold);
    text-transform: uppercase;
    line-height: 0.99;
  }
  .headline .strong {
    display: block;
    font-family: "Inter", Arial, sans-serif;
    font-weight: 800;
    font-size: 86px;
    letter-spacing: -1px;
  }
  .headline .light {
    display: block;
    font-family: "Inter", Arial, sans-serif;
    font-weight: 300;
    font-size: 84px;
    letter-spacing: -1px;
  }
  .intro {
    position: absolute;
    left: 72px;
    top: 640px;
    width: 790px;
    font-family: "Carlito", Calibri, sans-serif;
    font-size: 19px;
    line-height: 26px;
    color: var(--white);
  }
  .call {
    position: absolute;
    left: 88px;
    top: 864px;
    font-family: "Arimo", Arial, sans-serif;
  }
  .call .number {
    display: block;
    font-weight: 700;
    font-size: 35px;
    color: var(--gold);
  }
  .call .note {
    display: block;
    margin-top: 2px;
    font-size: 25px;
    color: var(--white);
  }
  .footer {
    position: absolute;
    left: 0; right: 0; bottom: 0;
    height: 217px;
    background: var(--paper);
  }
  .tagline {
    position: absolute;
    left: 90px;
    top: 58px;
    font-family: "Arimo", Arial, sans-serif;
    font-weight: 700;
    font-size: 22px;
    line-height: 26px;
    text-transform: uppercase;
    color: var(--tag-brown);
  }
  .brand-mark {
    position: absolute;
    left: 484px;
    top: 40px;
    width: 94px;
    height: 94px;
    border-radius: 50%;
    background: var(--ink);
  }
  .brand-divider {
    position: absolute;
    left: 635px;
    top: 2px;
    width: 1.5px;
    height: 170px;
    background: var(--ink);
  }
  .brand-name {
    position: absolute;
    left: 656px;
    top: 50px;
    font-family: "Arimo", Arial, sans-serif;
    font-weight: 400;
    font-size: 29px;
    line-height: 30px;
    text-transform: uppercase;
    color: var(--ink);
  }
</style>
</head>
<body>
  <main class="postcard">
    <div class="hero-photo" role="img" aria-label="Photograph of sprawling tree roots across sunlit park ground"></div>

    <h1 class="headline">
      <span class="strong">Long-Term</span>
      <span class="strong">Recovery</span>
      <span class="light">Starts</span>
      <span class="light">Growing Here!</span>
    </h1>

    <p class="intro">Did that statement give you HOPE?&nbsp; If it did, you have already started growing the roots needed for Long-Term Recovery.&nbsp; We believe that Recovery grows from Hope....the belief that Long-Term Recovery is real!&nbsp; And, by the way, it is real and it is attainable by anyone!!!&nbsp; Just as Substance Use Disorder (otherwise known as alcoholism and addiction) is real, so is Long-Term Recovery.&nbsp; Every facility we work with is hand chosen by us after a rigorous interview process, offering evidence based, 12-step based, Christian based and alternative healing approaches.&nbsp; Programs: Detox, In-Patient, PHP, IOP, Out Patient and Sober Living Communities.</p>

    <p class="call">
      <span class="number">Call 1-855-HARBR22</span>
      <span class="note">before you have to call 911".</span>
    </p>

    <footer class="footer">
      <p class="tagline">Long-Term Recovery<br>is our goal, not<br>temporary sobriety.</p>
      <div class="brand-mark" aria-hidden="true"></div>
      <div class="brand-divider" aria-hidden="true"></div>
      <p class="brand-name">Harbor<br>Wellness<br>Partners</p>
    </footer>
  </main>
</body>
</html>
```